Women's health flyer for Vindbro Health & Wellness . for a Women's health conference

I need a flyer , post card 4x 6 or 5 x 7 sized designed , 2 sides focused on my business branding and Women's health. we deliver bespoke care and focus on all phases of women's health and life. I want something aligned with our bespoke whole person care philosophy and that is fresh and forward thinking.
www.vindbro-example.com
This is to help women know they can have care for all phases of life , fertility , postpartum , perimenopause , mental health , wellness, weight loss, increased energy stress , menopause etc
please use knowledge from website about my company , www.vindbro-example.com
I also feel like my brand kit could use an additional secondarily color option in it

Target Market(s)

Women 25-70

Industry/Entity Type

health & Wellness

Colors
0054AA
0677BA
7BADD7
CADEEF
E8F1F8
0094D4
00A9DD
6FCCEA
C7EBF8
E9F6FB
00AB8E
00BBA5
67D7C9
C6EFE9
E9F9F6
59FF00
82FF00
B8FF75
E3FFCB
F4FFEA
E54698
E96AAD
F1A4CE
F9D9EA
FCEFF6
A7469A
B969AE
D3A5CF
EDDBEB
F8F0F9

Requirements
Must have
• photos , my logo, connection to my brand
Nice to have
• something fresh and different
Should not have
• look like a genetic "wellness program"

```html
<!DOCTYPE html>
<html lang="en">
<head>
<meta charset="utf-8">
<title>Vindbro Health &amp; Wellness – Postcard</title>
<link href="https://fonts.googleapis.com/css2?family=Montserrat:wght@400;500;600;700;800&display=swap" rel="stylesheet">
<style>
:root{
  --stage:#3a3a3a;
  --paper:#ffffff;
  --mist:#f2f7fa;
  --brand-blue:#15679a;
  --brand-green:#6ab547;
  --ink:#2f2f2f;
  --sand-light:#e2c79b;
  --sand-dark:#b8935e;
  --dot:#555;
}
*{margin:0;padding:0;box-sizing:border-box}
html,body{width:1200px;height:1200px;overflow:hidden}
body{background:var(--stage);font-family:'Montserrat',sans-serif;position:relative;color:var(--ink)}
.card{position:absolute;left:253px;width:701px;height:507px;background:var(--paper);overflow:hidden;box-shadow:0 6px 18px rgba(0,0,0,.35)}
.card--front{top:63px;background:linear-gradient(90deg,var(--mist),#fbfdfe 60%)}
.card--back{top:639px}

/* front */
.beach-photo{position:absolute;right:0;top:0;width:300px;height:507px;
  background:linear-gradient(160deg,var(--sand-light),#d8b883 50%,var(--sand-dark));
  clip-path:polygon(40% 0,34% 12%,28% 22%,24% 34%,20% 46%,15% 58%,12% 70%,10% 82%,8% 100%,100% 100%,100% 0)}
.leaf-decor{position:absolute;top:0;left:190px;width:511px;height:80px;
  background:linear-gradient(180deg,rgba(124,198,62,.35),rgba(124,198,62,0))}
.brand-mark{position:absolute;left:105px;top:22px;width:52px;height:52px;border-radius:50%;background:#6fcfea}
.brand-name{position:absolute;left:25px;top:108px;width:240px;text-align:center;font-weight:700;color:var(--brand-blue);line-height:1.1;white-space:nowrap}
.brand-name .word{display:block;font-size:36px;letter-spacing:1px}
.brand-name .tag{display:block;font-size:10px;letter-spacing:4px;margin-top:4px}
.headline{position:absolute;left:25px;top:196px;font-weight:800;font-size:46px;line-height:50px;letter-spacing:-.3px;white-space:nowrap}
.headline .line-blue{color:var(--brand-blue);display:block}
.headline .line-green{color:var(--brand-green);display:block}
.intro{position:absolute;left:25px;top:308px;width:392px;font-size:14.5px;line-height:21.5px;font-weight:500}
.rally{position:absolute;left:25px;top:398px;font-size:18px;font-weight:700;white-space:nowrap}
.url-pill{position:absolute;left:0;top:439px;width:290px;height:34px;background:var(--brand-blue);border-radius:0 17px 17px 0;
  color:#fff;font-weight:800;font-size:14px;letter-spacing:1.2px;display:flex;align-items:center;padding-left:24px;white-space:nowrap;box-shadow:3px 6px 8px rgba(0,0,0,.2)}

/* back */
.shore-photo{position:absolute;left:0;top:60px;width:440px;height:394px;
  background:linear-gradient(180deg,rgba(255,255,255,0) 0%,rgba(215,225,228,.55) 45%,rgba(225,220,210,.5) 100%)}
.leaf-decor--back{position:absolute;top:0;left:330px;width:340px;height:60px;background:linear-gradient(180deg,rgba(124,198,62,.3),rgba(124,198,62,0))}
.section-tab{position:absolute;left:0;width:223px;height:28px;background:var(--brand-green);border-radius:0 14px 14px 0;
  color:#fff;font-weight:700;font-size:23px;padding-left:27px;line-height:28px;white-space:nowrap;box-shadow:3px 5px 7px rgba(0,0,0,.18)}
.services{position:absolute;left:27px;top:64px;list-style:none;font-size:14.5px}
.services li{position:relative;padding-left:14px;font-weight:700;margin-bottom:10px;line-height:19px;white-space:nowrap}
.services li::before{content:"";position:absolute;left:0;top:6px;width:7px;height:7px;border-radius:50%;background:var(--brand-green)}
.services .mode{font-weight:400;margin-left:5px}
.services .mode--below{display:block;margin-left:0}
.reasons{position:absolute;left:27px;top:303px;list-style:none}
.reasons li{display:flex;align-items:center;height:30px;margin-bottom:6px;font-size:15px;font-weight:600;white-space:nowrap}
.reasons svg{width:31px;height:31px;margin-right:12px;flex:none}
.stamp-box{position:absolute;left:539px;top:40px;width:138px;height:90px;border:1.5px solid #333}
.address-lines{position:absolute;left:446px;top:211px;width:232px}
.address-lines span{display:block;height:40px;border-top:1.5px dashed var(--dot)}
.contact-band{position:absolute;left:0;top:454px;width:556px;height:53px;background:var(--brand-blue);border-radius:0 40px 0 0;
  display:flex;align-items:center;padding-left:24px;gap:16px;color:#fff;font-size:12px;font-weight:500;white-space:nowrap}
.contact-band .item{display:flex;align-items:center;gap:6px;white-space:nowrap}
.contact-band svg{width:12px;height:12px;flex:none}
.back-mark{position:absolute;left:611px;top:388px;width:30px;height:30px;border-radius:50%;background:#6fcfea}
.back-brand{position:absolute;left:566px;top:425px;width:120px;text-align:center;color:var(--brand-blue);font-weight:700;line-height:1;white-space:nowrap}
.back-brand .word{display:block;font-size:20px}
.back-brand .tag{display:block;font-size:6px;letter-spacing:2px;margin-top:3px}
</style>
</head>
<body>

<section class="card card--front">
  <div class="beach-photo" role="img" aria-label="Photo of a woman in a flowing white dress dancing on a sandy beach with footprints and ocean foam"></div>
  <div class="leaf-decor" role="img" aria-label="Green bamboo leaves along the top edge"></div>
  <div class="brand-mark"></div>
  <div class="brand-name"><span class="word">VINDBRO</span><span class="tag">HEALTH &amp; WELLNESS</span></div>
  <h1 class="headline"><span class="line-blue">Bespoke Whole</span><span class="line-green">Person Care</span></h1>
  <p class="intro">Inspired by the metaphor of ships charting their paths in the ocean, Vindbro emphasizes the importance of honoring individual needs within the context of community and global impact.</p>
  <p class="rally">Join us in this revolution of wellbeing</p>
  <div class="url-pill">www.vindbro-example.com</div>
</section>

<section class="card card--back">
  <div class="shore-photo" role="img" aria-label="Faded photo of a woman in a sun hat and white dress walking along the shoreline"></div>
  <div class="leaf-decor--back" role="img" aria-label="Soft-focus green leaves along the top edge"></div>

  <h2 class="section-tab" style="top:26px">Our Services</h2>
  <ul class="services">
    <li>Customized Corporate Wellness<span class="mode mode--below">(In-person or virtual)</span></li>
    <li>Individual Coaching<span class="mode">(Virtual)</span></li>
    <li>Retreats<span class="mode">(In-person or virtual)</span></li>
    <li>Workshops<span class="mode">(In-person or virtual)</span></li>
    <li>Acupuncture &amp; Traditional East Asian Medicine<span class="mode mode--below">(In-person or virtual)</span></li>
  </ul>

  <h2 class="section-tab" style="top:263px">Why Choose Us</h2>
  <ul class="reasons">
    <li><svg viewBox="0 0 32 32"><circle cx="16" cy="16" r="14.5" fill="none" stroke="#15679a" stroke-width="1.5"/><circle cx="16" cy="16" r="6" fill="none" stroke="#6ab547" stroke-width="1.5"/></svg>Whole person Approach</li>
    <li><svg viewBox="0 0 32 32"><circle cx="16" cy="16" r="14.5" fill="none" stroke="#15679a" stroke-width="1.5"/><circle cx="16" cy="16" r="6" fill="none" stroke="#6ab547" stroke-width="1.5"/></svg>Revolutionary Designed Programs</li>
    <li><svg viewBox="0 0 32 32"><circle cx="16" cy="16" r="14.5" fill="none" stroke="#15679a" stroke-width="1.5"/><circle cx="16" cy="16" r="6" fill="none" stroke="#6ab547" stroke-width="1.5"/></svg>Comprehensive Support</li>
    <li><svg viewBox="0 0 32 32"><circle cx="16" cy="16" r="14.5" fill="none" stroke="#15679a" stroke-width="1.5"/><circle cx="16" cy="16" r="6" fill="none" stroke="#6ab547" stroke-width="1.5"/></svg>Community and Individuality</li>
  </ul>

  <div class="stamp-box"></div>
  <div class="address-lines"><span></span><span></span><span></span><span></span><span></span></div>

  <div class="contact-band">
    <span class="item"><svg viewBox="0 0 24 24"><path d="M6 2l4 5-2 3c1.5 3 3.5 5 6 6l3-2 5 4-3 4C10 21 3 14 2 5z" fill="#6ab547"/></svg>+1-555-014-2290</span>
    <span class="item"><svg viewBox="0 0 24 24"><circle cx="12" cy="12" r="10" fill="none" stroke="#6ab547" stroke-width="2"/><path d="M2 12h20M12 2c4 4 4 16 0 20M12 2c-4 4-4 16 0 20" fill="none" stroke="#6ab547" stroke-width="2"/></svg>www.vindbro-example.com</span>
    <span class="item"><svg viewBox="0 0 24 24"><rect x="2" y="5" width="20" height="14" fill="none" stroke="#6ab547" stroke-width="2"/><path d="M2 5l10 8 10-8" fill="none" stroke="#6ab547" stroke-width="2"/></svg>hello@vindbro-example.com</span>
  </div>

  <div class="back-mark"></div>
  <div class="back-brand"><span class="word">VINDBRO</span><span class="tag">HEALTH &amp; WELLNESS</span></div>
</section>

</body>
</html>
```